The Lanterns of Steady Craft Personal Growth Template

We are creating a two-page Word document titled 'The Lanterns of Steady Craft.' This guide/template should embody a professional, clear, and engaging design that facilitates learning and application of DEI principles within a business context.

Target Market(s)

Our primary users are middle to senior management professionals who are responsible for implementing and upholding DEI values within their teams and organizations. The design must resonate with this demographic, implying a sophisticated and functional aesthetic.

Industry/Entity Type

Healthcare, Counseling

Requirements
Must have
• Branding: Incorporate BRK colors for branding consistency. Ensure that the 'Lanterns of Steady Craft' is prominently featured within the design. Content Layout: We require a clean, clear, and logical layout that intuitively guides the user through the steps of the DEI Growth Matrix. Image Redesign: The images pertaining to the assessment and differentiation of self should be recreated to be high-resolution and professionally styled. They should directly support the content and be relatable to our target audience. Accessibility: The template must be easily navigable, with font sizes and styles that ensure readability and ADA compliance. Actionable Steps: Clearly define sections for 'Inspiration,' 'Goal,' and 'Daily Commitment' with examples provided, and allow for user interaction such as note-taking or checkboxes. Reflection Section: Include a 'Two-Week Reflection & Follow-up' section to encourage ongoing engagement with the tool.
Nice to have
• we would appreciate it if the 'Daily Biopsychosocial Commitment Table' could be adjusted to track actions over a four-week period, rather than daily, to align with managerial workflows.
Should not have
• Informal Graphics: Avoid the use of cartoons, silly icons, or figures that could detract from the professional tone of the document. Overcrowding: Prevent a cluttered design by balancing white space with content, ensuring the guide does not overwhelm the user.

```html
<!DOCTYPE html>
<html lang="en">
<head>
<meta charset="utf-8">
<title>DEI Growth Matrix – The Lanterns of Steady Craft</title>
<link href="https://fonts.googleapis.com/css2?family=Cinzel:wght@500;600&family=Poppins:wght@400;500;600;700&family=Source+Serif+4:wght@400&display=swap" rel="stylesheet">
<style>
:root{
  --gold:#b08538;
  --navy:#1f1d5a;
  --ink:#1b1b2e;
  --bio:#1a1a4e;
  --social:#5b80c9;
  --stage:#e8e8e8;
  --paper:#ffffff;
  --wash:#efefef;
  --rule:#c9c9cf;
  --muted:#5a5a66;
}
*{box-sizing:border-box;margin:0;padding:0}
html,body{width:1200px;height:931px;overflow:hidden;background:var(--stage)}
body{font-family:'Poppins',sans-serif;color:var(--ink)}
.page{position:absolute;left:57px;top:58px;width:1092px;height:820px;background:var(--paper)}
.abs{position:absolute}

/* header */
.brand-left{left:70px;top:10px;width:150px;text-align:center}
.brand-left .mark{width:66px;height:66px;border:3px solid var(--navy);border-radius:50%;margin:0 auto 8px}
.brand-left .name{font-family:'Cinzel',serif;font-weight:600;color:var(--navy);font-size:12.5px;line-height:1.15}
.title-band{left:246px;top:0;width:599px;height:113px;background:var(--gold);border-radius:0 0 8px 8px;color:#fff;text-align:center;font-family:'Cinzel',serif;font-weight:500}
.title-band .l1{position:absolute;top:48px;left:0;right:0;font-size:19px;letter-spacing:.5px;display:flex;align-items:center;justify-content:center;gap:10px}
.title-band .l1 i{display:block;width:138px;height:1px;background:#fff}
.title-band .l2{position:absolute;top:73px;left:0;right:0;font-size:19.5px;letter-spacing:.8px}
.brand-right{left:870px;top:24px;width:165px;display:flex;align-items:center;gap:8px}
.brand-right .mark{width:44px;height:44px;border-radius:50%;border:4px solid var(--navy);flex:none}
.brand-right .name{font-weight:700;color:var(--navy);font-size:14px;line-height:1.1}
.tagline{left:864px;top:84px;width:170px;font-size:7.8px;font-weight:600;color:var(--navy);text-align:center;letter-spacing:.1px}

.purpose{left:69px;top:133px;font-size:10.3px;color:var(--ink);white-space:nowrap}

/* steps */
.step{display:flex;align-items:center;gap:10px;font-size:16.5px;font-weight:700}
.step .num{color:var(--navy)}
.step .lbl{color:var(--gold);font-weight:600}
.step svg{width:20px;height:20px}
.step-desc{font-size:10.6px;line-height:1.22;color:var(--ink)}

/* assessment */
.panel-title{font-size:17px;color:var(--navy);text-align:center;line-height:1.12}
.assess{left:109px;top:290px;width:402px;border-collapse:collapse;font-family:'Source Serif 4',serif;font-size:7px;color:var(--muted);table-layout:fixed}
.assess th{font-family:'Poppins',sans-serif;color:#fff;font-weight:500;font-size:11px;height:22px;border:1px solid var(--rule)}
.assess th.bio{background:var(--bio)}
.assess th.psy{background:var(--gold)}
.assess th.soc{background:var(--social)}
.assess td{border:1px solid var(--rule);vertical-align:top;padding:3px 4px 3px 16px;height:42px;line-height:1.33;position:relative}
.assess td::before{content:"•";position:absolute;left:5px;top:2px;color:var(--ink)}

/* differentiation */
.diff-sub{font-size:9px;color:var(--gold);text-align:center}
.tag{height:15px;font-size:6px;color:#fff;display:flex;align-items:center;justify-content:center}
.tag.left{background:var(--navy);clip-path:polygon(0 0,92% 0,100% 50%,92% 100%,0 100%)}
.tag.right{background:var(--gold);clip-path:polygon(8% 0,100% 0,100% 100%,8% 100%,0 50%)}
.traits{font-size:7px;line-height:1.3;color:var(--navy)}
.traits p{margin-bottom:3px}
.benefits{font-size:7px;line-height:1.3;color:var(--gold);text-align:right}
.benefits p{margin-bottom:3px}
.photo{background:linear-gradient(160deg,#d8d4cc,#8e7464 55%,#4e4a55);border:2px solid var(--social)}
.side-rule{width:2px;background:var(--navy)}

/* commitment table */
.commit{left:70px;top:530px;width:951px;height:274px;border:1.3px solid var(--navy)}
.commit .head{position:absolute;left:0;top:0;right:0;height:30px;background:var(--gold);display:flex}
.commit .head div{color:#fff;font-weight:700;font-size:13.5px;display:flex;align-items:center;justify-content:center}
.commit .col{position:absolute;top:30px;height:204px}
.commit .col + .col{border-left:1.3px solid var(--navy)}
.commit .intro{height:58px;padding:9px 26px 0;font-size:11px;line-height:1.15;color:var(--navy);text-align:justify;background:var(--paper)}
.commit .ex{height:146px;background:var(--wash);padding:12px 26px 0}
.commit .ex h4{font-weight:500;font-size:13px;color:var(--ink);margin-bottom:12px}
.commit .ex li{list-style:none;font-size:11.7px;line-height:1.17;padding-left:12px;position:relative;margin-bottom:13px}
.commit .ex li svg{position:absolute;left:0;top:4px;width:7px;height:7px}
.commit .reflect{position:absolute;left:0;right:0;bottom:0;height:40px;border-top:1.3px solid var(--navy);background:var(--wash);padding:10px 25px;font-weight:700;font-size:14px;color:var(--navy)}
</style>
</head>
<body>
<main class="page">

  <header>
    <div class="abs brand-left">
      <div class="mark"></div>
      <div class="name">THE LANTERNS OF STEADY CRAFT</div>
    </div>
    <div class="abs title-band">
      <div class="l1"><i></i>DEI GROWTH MATRIX :<i></i></div>
      <div class="l2">A BIOPSYCHOSOCIAL &amp; DIFFERENTIATION FRAMEWORK</div>
    </div>
    <div class="abs brand-right">
      <div class="mark"></div>
      <div class="name">THE HARBOR LOOM GROUP INC.</div>
    </div>
    <div class="abs tagline">CELEBRATING 40 YEARS OF INCLUSION</div>
  </header>

  <p class="abs purpose">Purpose: This template is designed to help individuals integrate DEI principles into their professional lives by identifying and committing to personal growth areas aligned with Systems and Bowen Theory.</p>

  <!-- Step 1 -->
  <section>
    <div class="abs step" style="left:117px;top:165px">
      <span class="num">STEP 1:</span>
      <svg viewBox="0 0 20 20" aria-hidden="true"><circle cx="10" cy="11" r="5" fill="none" stroke="#b08538" stroke-width="2"/><path d="M10 1v3M2 5l2 2M18 5l-2 2M7 17h6" stroke="#b08538" stroke-width="2"/></svg>
      <span class="lbl">INSPIRATION</span>
    </div>
    <p class="abs step-desc" style="left:117px;top:201px;width:400px">Examine the bio-psycho-social assessment and identify areas to improve your ability to contribute to a DEI-focused work environment</p>
    <h3 class="abs panel-title" style="left:110px;top:244px;width:400px;font-weight:400">Leaders Renew Spirit, Build Resilience and<br>Foster Well-Being</h3>
    <table class="abs assess">
      <thead><tr><th class="bio">Bio</th><th class="psy">Psycho</th><th class="soc">Social</th></tr></thead>
      <tbody>
        <tr>
          <td>I am aware of how family, culture, and experiences affect how I think and behave.</td>
          <td>I foster a psychologically safe environment to acknowledge, discuss and address emotional and polarizing issues.</td>
          <td>I consistently find ways to show appreciation during stressful and uncertain situations.</td>
        </tr>
        <tr>
          <td>I am aware of neurodiversity and how to leverage it for success.</td>
          <td>I instill the confidence that views and perspectives will be acknowledged and considered.</td>
          <td>I cultivate a broad and culturally diverse network of individuals to exchange ideas and make decisions.</td>
        </tr>
        <tr>
          <td>I nurture body and spirit in a manner that fosters hope, empathy, and grace.</td>
          <td>I am aware of unique talent(s), or strength(s) and how to nurture them.</td>
          <td>I use my power in visible and subtle ways to include people and discourage exclusion.</td>
        </tr>
      </tbody>
    </table>
  </section>

  <!-- Step 2 -->
  <section>
    <div class="abs step" style="left:589px;top:165px">
      <span class="num">STEP 2:</span>
      <svg viewBox="0 0 20 20" aria-hidden="true"><circle cx="10" cy="10" r="8" fill="none" stroke="#b08538" stroke-width="2"/><circle cx="10" cy="10" r="4" fill="none" stroke="#b08538" stroke-width="2"/><path d="M10 10l8-8" stroke="#b08538" stroke-width="2"/></svg>
      <span class="lbl">GOAL</span>
    </div>
    <p class="abs step-desc" style="left:589px;top:201px;width:420px">Choose attributes from the 'Differentiation of Self' framework that will support your role in fostering a DEI culture at work.</p>
    <h3 class="abs panel-title" style="left:585px;top:244px;width:400px;font-weight:400;font-size:16.5px">Differentiation of Self (Fostering Uniqueness)</h3>
    <p class="abs diff-sub" style="left:585px;top:263px;width:400px">How do we foster “differentiation of self” for ourselves and others?</p>

    <div class="abs side-rule" style="left:583px;top:290px;height:18px"></div>
    <div class="abs tag left" style="left:592px;top:284px;width:128px">“Differentiation of Self” Characteristics</div>
    <div class="abs traits" style="left:595px;top:304px;width:120px">
      <p>Be an interdependent member of the group.</p>
      <p>Maintain beliefs and attitudes in the face of pressure to conform.</p>
      <p>Resolve problems rather than let them fester.</p>
      <p>Self-validate.</p>
      <p>Self-soothe</p>
      <p>Tolerate short-term discomfort, or gratification for long-term growth</p>
      <p>Taking action</p>
    </div>

    <div class="abs photo" role="img" aria-label="Photo of a professional presenting to colleagues seated around a meeting table" style="left:725px;top:287px;width:121px;height:141px"></div>

    <div class="abs tag right" style="left:852px;top:284px;width:127px">“Differentiation of Self” Benefits</div>
    <div class="abs benefits" style="left:858px;top:305px;width:116px">
      <p>A sense of congruence within yourself = pride and confidence in yourself</p>
      <p>Highly self-aware = greater capacity to be aware of others</p>
      <p>Highly differentiated = better at handling stress/anxiety</p>
      <p>Positive feelings can become self-perpetuating.</p>
      <p>Increased differentiation by one member will likely lead other members to become more differentiated.</p>
      <p>Ownership of self</p>
    </div>
  </section>

  <!-- Step 3 -->
  <section>
    <div class="abs step" style="left:70px;top:459px">
      <span class="num">STEP 3:</span>
      <svg viewBox="0 0 20 20" aria-hidden="true"><rect x="2" y="4" width="16" height="14" rx="1" fill="none" stroke="#b08538" stroke-width="2"/><path d="M2 8h16M6 2v4M14 2v4" stroke="#b08538" stroke-width="2"/></svg>
      <span class="lbl">DAILY COMMITMENT</span>
    </div>
    <p class="abs step-desc" style="left:70px;top:492px;white-space:nowrap">Define specific, daily actions to help you work towards your well-being and differentiation goals, ultimately enhancing DEI implementation in your job.</p>

    <div class="abs commit">
      <div class="head">
        <div style="width:311px">BIO</div>
        <div style="width:323px">PSYCHO</div>
        <div style="width:317px">SOCIAL</div>
      </div>

      <div class="col" style="left:0;width:311px">
        <p class="intro">In the 'Bio' category, actions could include self-care practices that enable one to be an effective DEI advocate even under stress.</p>
        <div class="ex">
          <h4>EXAMPLES INCLUDE:</h4>
          <ul>
            <li><svg viewBox="0 0 8 8"><circle cx="4" cy="4" r="3.4" fill="none" stroke="#1b1b2e" stroke-width=".8"/><path d="M2.3 4.1l1.2 1.1 2.3-2.4" fill="none" stroke="#1b1b2e" stroke-width=".8"/></svg>Practice mindfulness to maintain resilience when discussing DEI topics in polarized settings.</li>
            <li><svg viewBox="0 0 8 8"><circle cx="4" cy="4" r="3.4" fill="none" stroke="#1b1b2e" stroke-width=".8"/><path d="M2.3 4.1l1.2 1.1 2.3-2.4" fill="none" stroke="#1b1b2e" stroke-width=".8"/></svg>Engage in physical activities that improve mental clarity to approach DEI work with a non-anxious presence.</li>
          </ul>
        </div>
      </div>

      <div class="col" style="left:311px;width:323px">
        <p class="intro">'Psycho' actions may involve education and reflection on one's cultural competencies and biases.</p>
        <div class="ex">
          <h4>EXAMPLES INCLUDE:</h4>
          <ul>
            <li><svg viewBox="0 0 8 8"><circle cx="4" cy="4" r="3.4" fill="none" stroke="#1b1b2e" stroke-width=".8"/><path d="M2.3 4.1l1.2 1.1 2.3-2.4" fill="none" stroke="#1b1b2e" stroke-width=".8"/></svg>Reflect daily on personal biases to foster a mindset open to DEI learning and transformation.</li>
            <li><svg viewBox="0 0 8 8"><circle cx="4" cy="4" r="3.4" fill="none" stroke="#1b1b2e" stroke-width=".8"/><path d="M2.3 4.1l1.2 1.1 2.3-2.4" fill="none" stroke="#1b1b2e" stroke-width=".8"/></svg>Write a journal about DEI progress to reinforce learning and personal growth in DEI competencies.</li>
          </ul>
        </div>
      </div>

      <div class="col" style="left:634px;width:315px">
        <p class="intro">'Social' commitments could be activities that promote inclusion and equity within one's immediate professional sphere.</p>
        <div class="ex">
          <h4>EXAMPLES INCLUDE:</h4>
          <ul>
            <li><svg viewBox="0 0 8 8"><circle cx="4" cy="4" r="3.4" fill="none" stroke="#1b1b2e" stroke-width=".8"/><path d="M2.3 4.1l1.2 1.1 2.3-2.4" fill="none" stroke="#1b1b2e" stroke-width=".8"/></svg>Initiate conversations about DEI with colleagues to understand diverse perspectives.</li>
            <li><svg viewBox="0 0 8 8"><circle cx="4" cy="4" r="3.4" fill="none" stroke="#1b1b2e" stroke-width=".8"/><path d="M2.3 4.1l1.2 1.1 2.3-2.4" fill="none" stroke="#1b1b2e" stroke-width=".8"/></svg>Lead by example in inclusive behaviors, ensuring all team members feel valued and heard.</li>
          </ul>
        </div>
      </div>

      <div class="reflect">TWO-WEEK REFLECTION&amp; FOLLOW</div>
    </div>
  </section>

</main>
</body>
</html>
```